Invoice design

Please design an invoice like the attached

- Please include a logo in the header (any logo rectangular is fine)

- We do not need a DUE DATE on the invoice (next to the total inc. vat)

- For each product put in smaller text beneath which might contain additional information about the product (e.g. size, colour choices)

- Do not put a signature in the footer

```html
<!DOCTYPE html>
<html lang="en">
<head>
<meta charset="utf-8">
<title>Invoice 00001 – Norvale Ltd</title>
<link href="https://fonts.googleapis.com/css2?family=Montserrat:wght@400;500;600;700;800&display=swap" rel="stylesheet">
<style>
  :root {
    --backdrop: #c9c9c9;
    --paper: #ffffff;
    --blue: #1287b8;
    --blue-light: #149ac8;
    --blue-dark: #127fb0;
    --navy: #0b3866;
    --ink: #2b2b2b;
    --rule: #8a8a8a;
    --rule-light: #cfcfcf;
  }
  * { box-sizing: border-box; margin: 0; padding: 0; }
  html, body { width: 1110px; height: 1200px; overflow: hidden; }
  body {
    background: var(--backdrop);
    font-family: "Montserrat", sans-serif;
    color: var(--ink);
    position: relative;
  }
  .page {
    position: absolute;
    left: 162px; top: 46px;
    width: 784px; height: 1107px;
    background: var(--paper);
    box-shadow: 6px 8px 14px rgba(0,0,0,0.28);
  }
  .abs { position: absolute; }
  .title-band {
    left: 0; top: 0; width: 784px; height: 75px;
    background: linear-gradient(90deg, var(--blue-dark), var(--blue-light));
    color: #fff; text-align: center;
    font-weight: 700; font-size: 46px; letter-spacing: 3px; line-height: 75px;
  }
  .brand {
    left: 0; width: 784px; text-align: center;
    color: var(--navy); font-weight: 700;
  }
  .brand-mark {
    display: inline-block; background: var(--navy);
    vertical-align: middle; margin-right: 12px;
  }
  .brand-top { top: 120px; font-size: 35px; line-height: 50px; }
  .brand-top .brand-mark { width: 26px; height: 26px; }
  .brand-bottom { top: 940px; font-size: 27px; line-height: 44px; }
  .brand-bottom .brand-mark { width: 20px; height: 20px; }
  .label { color: var(--blue); font-weight: 500; font-size: 13.5px; letter-spacing: 0.2px; }
  .meta { left: 44px; top: 218px; }
  .meta .label { margin-top: 6px; line-height: 17px; }
  .meta .label:first-child { margin-top: 0; }
  .meta .value { font-size: 13.5px; font-weight: 500; line-height: 16px; margin-top: 0; }
  .meta .gap-lg { margin-top: 10px; }
  .divider { width: 1px; background: var(--rule); }
  .party { top: 214px; font-size: 12.3px; line-height: 18.2px; }
  .party .label { line-height: 20px; margin-bottom: 2px; }
  .party strong { font-weight: 600; }
  .supplier { left: 333px; }
  .client { left: 595px; }
  .items {
    left: 44px; top: 427px; width: 703px;
    border-collapse: collapse; table-layout: fixed;
  }
  .items th {
    background: linear-gradient(90deg, var(--blue-light), var(--blue-dark));
    color: #fff; font-weight: 500; font-size: 13.3px; height: 42px;
    border-left: 1.5px solid #fff;
  }
  .items th:first-child { border-left: 0; }
  .items td {
    border-left: 1px solid var(--rule-light);
    border-bottom: 1px solid var(--rule);
    text-align: center; font-size: 12.5px; height: 50px;
  }
  .items td:first-child { border-left: 0; text-align: left; padding-left: 7px; }
  .items td.num { font-size: 11px; font-weight: 600; }
  .items td.money { font-size: 11px; font-weight: 600; text-align: right; padding-right: 13px; }
  .product { font-size: 12px; font-weight: 500; line-height: 17px; }
  .product-detail { font-size: 12.5px; line-height: 17px; color: #444; }
  .product-detail span { display: inline-block; width: 84px; }
  .summary { left: 414px; top: 579px; width: 333px; }
  .summary-row {
    display: flex; justify-content: space-between; align-items: center;
    height: 39px; border-bottom: 1px solid var(--rule);
    font-size: 11.5px; padding-right: 13px;
  }
  .summary-row:last-child { border-bottom: 0; }
  .summary-row .label { font-size: 11.5px; }
  .summary-row .amount { font-weight: 600; }
  .grand-total {
    left: 51px; top: 761px; width: 696px; height: 50px;
    border: 1.5px dashed #8c8c8c;
    display: flex; justify-content: space-between; align-items: center;
    padding: 0 52px 0 27px;
  }
  .grand-total .label { font-size: 16px; padding-top: 4px; }
  .grand-total .amount { font-size: 24px; font-weight: 800; }
  .payment { top: 866px; font-size: 14px; }
  .payment .label { font-size: 14.5px; line-height: 20px; }
  .payment .value { font-weight: 500; line-height: 22px; }
  .footer-rule { left: 55px; top: 1003px; width: 672px; height: 1.5px; background: #2f6f9f; }
  .contacts {
    left: 0; top: 1012px; width: 784px;
    display: flex; justify-content: center; gap: 20px;
    font-size: 18px; line-height: 26px;
  }
  .contact { display: flex; align-items: center; gap: 6px; }
  .address { left: 0; top: 1039px; width: 784px; text-align: center; font-size: 18px; line-height: 26px; }
  .bottom-band { left: 0; top: 1081px; }
</style>
</head>
<body>
<main class="page">
  <header class="abs title-band">INVOICE</header>

  <div class="abs brand brand-top"><span class="brand-mark"></span>NORVALE</div>

  <section class="abs meta">
    <p class="label">INVOICE:</p>
    <p class="value">00001</p>
    <p class="label gap-lg">ISSUE DATE:</p>
    <p class="value">July 3, 2020</p>
    <p class="label gap-lg">DELIVERY DATE:</p>
    <p class="value">July 3, 2020</p>
    <p class="label gap-lg">DUE DATE:</p>
    <p class="value">July 18, 2020</p>
  </section>

  <div class="abs divider" style="left:258px; top:210px; height:167px;"></div>

  <section class="abs party supplier">
    <p class="label">SUPPLIER</p>
    <p><strong>Norvale Ltd</strong></p>
    <p>42 Larkhill Lane</p>
    <p>London</p>
    <p>EC1V 4PX</p>
    <p>United Kingdom</p>
    <p>VAT No: GB4815162342</p>
  </section>

  <div class="abs divider" style="left:540px; top:210px; height:167px;"></div>

  <section class="abs party client">
    <p class="label">CLIENT</p>
    <p><strong>Harriet Mallory</strong></p>
    <p><strong>The Copper Kettle</strong></p>
    <p>17 Alder Row</p>
    <p>London</p>
    <p>NW5 2QT</p>
    <p>United Kingdom</p>
    <p>VAT No: GB987 6543 21</p>
  </section>

  <table class="abs items">
    <colgroup>
      <col style="width:200px"><col style="width:131px"><col style="width:90px">
      <col style="width:149px"><col style="width:57px"><col style="width:76px">
    </colgroup>
    <thead>
      <tr><th>Item</th><th>Description</th><th>Quantity</th><th>Unit Price incl. VAT</th><th>VAT</th><th>Total</th></tr>
    </thead>
    <tbody>
      <tr>
        <td><p class="product">Highland Ridge Blend</p><p class="product-detail"><span>size:</span>color:</p></td>
        <td>1 kg/Full City</td><td>2</td><td class="num">15.00</td><td class="num">20%</td><td class="money">£30.00</td>
      </tr>
      <tr>
        <td><p class="product">Valle Verde - Las Palmas</p><p class="product-detail"><span>size:</span>color:</p></td>
        <td>1 kg/Full City</td><td>3</td><td class="num">65.00</td><td class="num">20%</td><td class="money">£195.00</td>
      </tr>
    </tbody>
  </table>

  <section class="abs summary">
    <div class="summary-row"><span class="label">SUBTOTAL:</span><span class="amount">£225.00</span></div>
    <div class="summary-row"><span class="label">SHIPPING:</span><span class="amount">£18.00</span></div>
    <div class="summary-row"><span class="label">TOTAL EXCL. VAT:</span><span class="amount">£205.00</span></div>
    <div class="summary-row"><span class="label">VAT 20%:</span><span class="amount">£37.50</span></div>
  </section>

  <section class="abs grand-total">
    <span class="label">TOTAL INCL. VAT:</span>
    <span class="amount">£243.00</span>
  </section>

  <section class="abs payment" style="left:53px;">
    <p class="label">PAYMENT METHOD</p><p class="value">Bank Transfer</p>
  </section>
  <div class="abs divider" style="left:247px; top:864px; height:41px;"></div>
  <section class="abs payment" style="left:331px;">
    <p class="label">BANK ACCOUNT</p><p class="value">0000 0000 0000 00</p>
  </section>
  <div class="abs divider" style="left:554px; top:864px; height:41px;"></div>
  <section class="abs payment" style="left:626px;">
    <p class="label">ORDER NUMBER</p><p class="value">#0000</p>
  </section>

  <div class="abs brand brand-bottom"><span class="brand-mark"></span>NORVALE</div>

  <div class="abs footer-rule"></div>

  <div class="abs contacts">
    <span class="contact">
      <svg width="20" height="20" viewBox="0 0 24 24" aria-hidden="true"><path fill="#1a8cc0" d="M6.6 10.8a15.1 15.1 0 0 0 6.6 6.6l2.2-2.2c.3-.3.7-.4 1-.2 1.1.4 2.3.6 3.6.6.6 0 1 .4 1 1V20c0 .6-.4 1-1 1A17 17 0 0 1 3 4c0-.6.4-1 1-1h3.5c.6 0 1 .4 1 1 0 1.3.2 2.5.6 3.6.1.3 0 .7-.2 1z"/></svg>
      (000) 000 0000
    </span>
    <span class="contact">
      <svg width="20" height="14" viewBox="0 0 20 14" aria-hidden="true"><rect x="0.5" y="0.5" width="19" height="13" fill="#1a8cc0"/><path d="M1 1l9 7 9-7M1 13l6.5-6M19 13l-6.5-6" stroke="#fff" stroke-width="1.3" fill="none"/></svg>
      email@company.com
    </span>
    <span class="contact">
      <svg width="20" height="20" viewBox="0 0 20 20" aria-hidden="true"><g fill="none" stroke="#1a8cc0" stroke-width="1.6"><circle cx="10" cy="10" r="8.5"/><ellipse cx="10" cy="10" rx="3.8" ry="8.5"/><path d="M1.5 10h17M3 5.5h14M3 14.5h14"/></g></svg>
      www.company.com
    </span>
  </div>

  <p class="abs address">Company Name - 123 Name Street, 000 Your City, 00000-000</p>

  <svg class="abs bottom-band" width="786" height="27" viewBox="0 0 786 27" aria-hidden="true">
    <defs>
      <linearGradient id="band-light" x1="0" x2="1" y1="0" y2="0">
        <stop offset="0" stop-color="#149ac8"/><stop offset="1" stop-color="#127fb0"/>
      </linearGradient>
    </defs>
    <polygon points="0,1 517,1 502,27 0,27" fill="url(#band-light)"/>
    <polygon points="532,0 786,0 786,27 512,27" fill="#0b3866"/>
  </svg>
</main>
</body>
</html>
```